Website Templates Design Project

PeakForge Template Websites
Creative Brief

PeakForge Gyms
The growth of PeakForge Gyms (or boxes, as they are called by members) is an amazing world-wide phenomenon. More than 3,400 gyms ranging from “garage gyms” to massive retail locations have opened in recent years. The philosophy for workouts at the gym is built around is “constantly varied (if not random), high intensity, functional movement". Each gym does what is called a WOD, or Workout of the Day. Workouts are typically short—20 minutes or less—and intense, demanding all-out physical exertion.
The growth of the gyms, mainly in the United States, has generally come from military veterans, police officers and fireman. However, PeakForge box owners are mostly trainers and not necessarily skilled in operating or marketing a business. Our company is launching a new platform for boxes to purchase inexpensive template websites and other marketing materials.
The Need
Most PeakForge box owners have launched with basic WordPress websites. We see an opportunity to provide more dynamic and professional websites, using a template and content management system. We aim to offer multiple template designs (not WordPress) for box owners. The platform that we are using can be found at www.tealmockup47.com. We are looking for graphic designs that will fit this platform.
A big part of the PeakForge philosophy is built around an Internet-based community. Therefore, our website templates should allow for a robust blog that allows for posting of pictures and video by members and the box owner.
The Designs
We strongly encourage designers to review other PeakForge websites for design ideas and functionality (good and bad).
We are looking for cutting-edge designs. One person on our team said, “these sites need to be so good that they sweat!” Obviously, imagery that portrays working out and muscles will be attractive to box owners. Many of the graphics for PeakForge sites use particularly masculine images like diamond plate and steel. The designs should be contemporary and at first glance you show know that this is a PeakForge website.
Rotating images and video windows are good, just nothing that will require long load times.

Images and Logos
Please don’t pirate logos ad images from PeakForge sites without permission. For your design submissions, feel free to develop generic logos and names for PeakForge Gyms. If you use and stock photography, please indicate whether you have permission to use or where permission can be obtained.

The navigation for a basic website design (and your designs) should include:
Home (with WOD blog dominating body of page)
About Us
Store
Membership Info (with link to store)
Directions
Contact Us

Target Market(s)

18-35, athletic types, male and female

Industry/Entity Type

Marketing

Requirements
Must have
• Navigation "buttons":

About Us
Store
Directions
Contact Us

```html
<!DOCTYPE html>
<html lang="en">
<head>
<meta charset="utf-8">
<title>PeakForge Gyms</title>
<link href="https://fonts.googleapis.com/css2?family=Alfa+Slab+One&family=Arvo&family=Bebas+Neue&family=Open+Sans:wght@300;700&display=swap" rel="stylesheet">
<style>
  :root {
    --page-bg: #262626;
    --column-top: #b0b0b0;
    --column-bottom: #5c5c5c;
    --brand-red: #8b0000;
    --nav-bg: #3b3b3b;
    --panel-bg: #f2f2f2;
    --text-body: #5a5a5a;
    --text-dark: #1a1a1a;
    --field-border: #d4d4d4;
    --footer-bg: #050505;
    --copyright: #e23a2a;
  }
  * { box-sizing: border-box; margin: 0; padding: 0; }
  html, body { width: 1200px; height: 886px; overflow: hidden; }
  body {
    position: relative;
    background: radial-gradient(circle at 50% 40%, #333 0%, var(--page-bg) 70%);
    font-family: "Open Sans", Arial, sans-serif;
  }
  .top-bar { position: absolute; left: 0; top: 0; width: 1200px; height: 7px; background: var(--brand-red); }
  .column {
    position: absolute; left: 172px; top: 7px; width: 859px; height: 879px;
    background: linear-gradient(180deg, var(--column-top) 0%, #9a9a9a 45%, var(--column-bottom) 100%);
  }
  .social-tab { position: absolute; left: 860px; top: 7px; width: 157px; height: 27px; }
  .logo {
    position: absolute; left: 187px; top: 52px; display: flex; align-items: center; gap: 10px;
    font-family: "Bebas Neue", sans-serif; font-size: 34px; color: var(--text-dark); letter-spacing: 1px;
  }
  .logo-mark { width: 46px; height: 46px; border-radius: 50%; background: #555; }
  .main-nav {
    position: absolute; left: 449px; top: 56px; width: 568px; height: 44px;
    background: var(--nav-bg); border-radius: 4px;
  }
  .main-nav a {
    position: absolute; top: 10px; font-family: "Bebas Neue", sans-serif; font-size: 24px;
    color: #fff; text-decoration: none; line-height: 1;
  }
  .hero { position: absolute; left: 184px; top: 125px; width: 834px; height: 300px; }
  .content-panel {
    position: absolute; left: 184px; top: 446px; width: 834px; height: 360px;
    background: var(--panel-bg); border-radius: 4px;
  }
  .welcome-title {
    position: absolute; left: 28px; top: 22px; font-family: "Arvo", serif; font-weight: 400;
    font-size: 29px; color: var(--text-dark);
  }
  .welcome-title span { color: var(--brand-red); }
  .welcome-copy p {
    position: absolute; left: 28px; width: 495px; font-size: 11.3px; line-height: 14px;
    font-weight: 300; color: var(--text-body); text-align: justify;
  }
  .quick-contact { position: absolute; left: 742px; top: 478px; width: 285px; height: 50px; }
  .contact-form .field {
    position: absolute; left: 757px; width: 244px; background: #fff; border: 1px solid var(--field-border);
    border-radius: 2px; font-size: 12px; font-style: italic; font-weight: 300; color: #666;
    padding: 10px 10px;
  }
  .submit-btn {
    position: absolute; left: 757px; top: 749px; width: 99px; height: 37px; background: var(--brand-red);
    color: #fff; font-weight: 700; font-size: 16px; display: flex; align-items: center; justify-content: center;
    border-radius: 2px;
  }
  .site-footer {
    position: absolute; left: 184px; top: 817px; width: 834px; height: 51px; background: var(--footer-bg);
    border-radius: 4px;
  }
  .footer-nav a {
    position: absolute; top: 21px; font-size: 9.5px; color: #fff; text-decoration: none; line-height: 1;
  }
  .copyright { position: absolute; right: 12px; top: 21px; font-size: 9.5px; color: var(--copyright); line-height: 1; }
</style>
</head>
<body>
  <div class="top-bar"></div>
  <div class="column"></div>

  <svg class="social-tab" viewBox="0 0 157 27" aria-label="Social links">
    <polygon points="0,0 157,0 143,27 12,27" fill="var(--brand-red)"/>
    <circle cx="37" cy="13" r="6" fill="#fff"/>
    <circle cx="75" cy="13" r="6" fill="#fff"/>
    <circle cx="112" cy="13" r="6" fill="#fff"/>
  </svg>

  <div class="logo"><span class="logo-mark"></span>PeakForge Gyms</div>

  <nav class="main-nav">
    <a style="left:16px">Home</a>
    <a style="left:76px">About Us</a>
    <a style="left:164px">Store</a>
    <a style="left:228px">Membership Info</a>
    <a style="left:371px">Directions</a>
    <a style="left:473px">Contact Us</a>
  </nav>

  <svg class="hero" viewBox="0 0 834 300">
    <defs>
      <linearGradient id="steel" x1="0" y1="0" x2="0" y2="1">
        <stop offset="0" stop-color="#b8b8b8"/><stop offset="1" stop-color="#8a8a8a"/>
      </linearGradient>
      <linearGradient id="skinLeft" x1="0" y1="0" x2="1" y2="1">
        <stop offset="0" stop-color="#c77a45"/><stop offset="1" stop-color="#6e3a1c"/>
      </linearGradient>
      <linearGradient id="skinRight" x1="1" y1="0" x2="0" y2="1">
        <stop offset="0" stop-color="#a86a4a"/><stop offset="1" stop-color="#5e3525"/>
      </linearGradient>
    </defs>
    <rect x="0" y="0" width="834" height="300" fill="#0c0c0c"/>
    <rect x="0" y="0" width="834" height="11" fill="url(#steel)"/>
    <rect x="0" y="289" width="834" height="11" fill="url(#steel)"/>
    <rect role="img" aria-label="Photo of a muscular athlete lifting a dumbbell" x="0" y="11" width="300" height="278" fill="url(#skinLeft)"/>
    <polygon points="0,259 560,195 834,180 834,289 0,289" fill="var(--brand-red)"/>
    <rect role="img" aria-label="Photo of a muscular athlete in sunglasses" x="560" y="11" width="274" height="278" fill="url(#skinRight)"/>
    <text x="295" y="133" font-family="Alfa Slab One, serif" font-size="96" fill="#fff" textLength="228" lengthAdjust="spacingAndGlyphs">HAVE</text>
    <text x="238" y="171" font-family="Alfa Slab One, serif" font-size="28" fill="#fff" textLength="285" lengthAdjust="spacingAndGlyphs">YOUR DAILY WORKOUT</text>
    <text transform="translate(549,62) rotate(90)" font-family="Alfa Slab One, serif" font-size="40" fill="var(--brand-red)" textLength="105" lengthAdjust="spacingAndGlyphs">WITH</text>
    <text transform="translate(531,62) rotate(90)" font-family="Alfa Slab One, serif" font-size="12" fill="var(--brand-red)" textLength="105" lengthAdjust="spacingAndGlyphs">PEAKFORGEGYMS</text>
  </svg>

  <section class="content-panel">
    <h1 class="welcome-title">Welcome to <span>PeakForgeGyms</span></h1>
    <div class="welcome-copy">
      <p style="top:77px">Lorem ipsum dolor sit amet, consectetur adipiscing elit. Integer non lacus neque. Nunc quis orci sed sem rhoncus facilisis. Sed magna sem, facilisis eget consequat sit amet, gravida ut eros. Aenean viverra, enim condimentum commodo placerat, nulla elit ornare diam, a vestibulum urna justo sed velit. In mollis, sem quis posuere lacinia, dolor erat lacinia turpis, at mattis nibh sem non eros. Duis iaculis placerat augue, quis sodales felis commodo ac.</p>
      <p style="top:161px">Proin molestie felis in eros consequat non porttitor dui posuere. Nullam faucibus nunc tortor, sed aliquet lectus. Proin sit amet enim nec erat gravida blandit. Phasellus ligula diam, lacinia nec vulputate vitae, gravida vitae dolor. Morbi nec turpis vitae enim pellentesque vestibulum.</p>
      <p style="top:217px">Fusce condimentum enim quis purus vehicula rutrum. Phasellus vehicula luctus augue in luctus. Quisque ipsum turpis, imperdiet eget faucibus et, dignissim quis risus.</p>
    </div>
  </section>

  <svg class="quick-contact" viewBox="0 0 285 50">
    <defs>
      <linearGradient id="ribbon" x1="0" y1="0" x2="1" y2="0">
        <stop offset="0" stop-color="#2c2c2c"/><stop offset="1" stop-color="#4a4a4a"/>
      </linearGradient>
    </defs>
    <polygon points="0,20 20,0 285,0 285,40 20,40" fill="url(#ribbon)"/>
    <polygon points="275,40 285,40 275,49" fill="#111"/>
    <text x="29" y="30" font-family="Arvo, serif" font-size="27" fill="#fff">Quick Contact</text>
  </svg>

  <form class="contact-form">
    <div class="field" style="top:542px;height:36px">Name</div>
    <div class="field" style="top:586px;height:36px">Email</div>
    <div class="field" style="top:631px;height:103px">Message</div>
    <div class="submit-btn">SUBMIT</div>
  </form>

  <footer class="site-footer">
    <nav class="footer-nav">
      <a style="left:12px">HOME</a>
      <a style="left:54px">ABOUT US</a>
      <a style="left:115px">STORE</a>
      <a style="left:161px">MEMBERSHIP INFO</a>
      <a style="left:254px">DIRECTIONS</a>
      <a style="left:320px">CONTACT US</a>
    </nav>
    <p class="copyright">Copyright 2012. PeakForgeGyms. All RightsReserved.</p>
  </footer>
</body>
</html>
```